Business Cards- The Manor at Brookridge Golf Club

We would like our business cards to look more high-end. We are a wedding venue that has been in business for 60+ years. We like our logo and our colors - primarily green and a touch of gold/beige. The owner wants our business cards to look more special..

Target Market(s)

Brides who have already toured our venue

Industry/Entity Type

Wedding venue - mansion

Contact Information for Business Card

Name, email, physical address, phone number

Colors
00AB8E
00BBA5
67D7C9
C6EFE9
E9F9F6

Requirements
Must have
• I think we would like our cards to be so pretty that people will want to keep them and will remember the venue. The venue is historic (built in 1850) and beautiful.
Nice to have
• Could we put an image of the building on one side and the contact info on the other?
Should not have
• The color black

```html
<!DOCTYPE html>
<html lang="en">
<head>
<meta charset="utf-8">
<title>The Manor at Brookridge Golf Club – Business Card</title>
<link rel="stylesheet" href="https://fonts.googleapis.com/css2?family=Cormorant+Garamond:ital,wght@1,500;1,600&display=swap">
<style>
  :root {
    --backdrop: #4a4b4d;
    --card-white: #ffffff;
    --sage: #93b46c;
    --sage-deep: #86a95e;
    --ink-green: #3c5a25;
    --logo-green: #7aa552;
    --gold: #b9a47c;
    --gold-light: #d9ccb0;
    --line-white: #f4f7ef;
  }
  * { box-sizing: border-box; margin: 0; padding: 0; }
  html, body { width: 1200px; height: 900px; overflow: hidden; }
  body {
    background: var(--backdrop);
    font-family: "Cormorant Garamond", Georgia, serif;
    position: relative;
  }
  .card {
    position: absolute;
    top: 110px;
    width: 390px;
    height: 680px;
    box-shadow: 0 14px 30px rgba(0,0,0,0.35);
  }
  .card--front { left: 170px; background: var(--card-white); }
  .card--back  { left: 640px; background: var(--sage); }

  /* gold frame with corner squares */
  .frame {
    position: absolute;
    inset: 14px;
    border: 2px solid var(--gold);
  }
  .frame__corner {
    position: absolute;
    width: 10px; height: 10px;
    background: var(--gold-light);
    border: 1px solid var(--gold);
    transform: rotate(45deg);
  }
  .frame__corner--tl { top: -6px; left: -6px; }
  .frame__corner--tr { top: -6px; right: -6px; }
  .frame__corner--bl { bottom: -6px; left: -6px; }
  .frame__corner--br { bottom: -6px; right: -6px; }
  .card--back .frame { border-color: var(--line-white); inset: 12px; }

  /* front: logo area */
  .brand {
    position: absolute;
    top: 70px; left: 30px; right: 30px;
    display: flex;
    align-items: center;
    justify-content: center;
    gap: 10px;
  }
  .brand__mark {
    width: 14px; height: 14px;
    border-radius: 50%;
    background: var(--gold);
    flex: none;
  }
  .brand__name {
    font-style: italic;
    font-weight: 600;
    font-size: 27px;
    line-height: 1.1;
    color: var(--logo-green);
    text-align: center;
  }

  /* front: contact panel */
  .contact-panel {
    position: absolute;
    left: 24px; right: 24px; bottom: 24px;
    height: 370px;
    background: var(--sage);
    color: var(--ink-green);
    font-style: italic;
    text-align: center;
    padding-top: 62px;
  }
  .contact-panel__name { font-size: 34px; font-weight: 600; }
  .contact-panel__title { font-size: 19px; font-weight: 500; margin-top: 2px; }
  .contact-list {
    list-style: none;
    margin-top: 56px;
    font-size: 19px;
    font-weight: 500;
    line-height: 1.55;
  }
  .contact-list li { display: flex; justify-content: center; align-items: flex-start; gap: 8px; }
  .contact-list svg { width: 16px; height: 16px; margin-top: 6px; flex: none; fill: var(--ink-green); }
  .contact-list .address { text-align: center; }

  /* back: photo area */
  .photo {
    position: absolute;
    inset: 24px;
    background: linear-gradient(160deg, #3d5668 0%, #7a3a2a 32%, #5a3424 55%, #d8cfc6 78%, #4a3526 100%);
  }
  .brand--overlay { top: 48px; }
  .brand--overlay .brand__name { color: var(--line-white); font-size: 25px; }
  .brand--overlay .brand__mark { background: var(--line-white); }
</style>
</head>
<body>

<section class="card card--front" aria-label="Business card, contact side">
  <div class="frame">
    <span class="frame__corner frame__corner--tl"></span>
    <span class="frame__corner frame__corner--tr"></span>
    <span class="frame__corner frame__corner--bl"></span>
    <span class="frame__corner frame__corner--br"></span>
  </div>

  <div class="brand">
    <span class="brand__name">The Manor at Brookridge Golf Club</span>
    <span class="brand__mark"></span>
  </div>

  <div class="contact-panel">
    <p class="contact-panel__name">Helen Whitaker</p>
    <p class="contact-panel__title">President/Owner</p>
    <ul class="contact-list">
      <li>
        <svg viewBox="0 0 16 16" aria-hidden="true"><path d="M2 6c0-2 3-3 6-3s6 1 6 3v1h-3V6H5v1H2z"/><rect x="3" y="8" width="10" height="6" rx="1"/></svg>
        <span>(410) 555-0148</span>
      </li>
      <li>
        <svg viewBox="0 0 16 16" aria-hidden="true"><path d="M1 4h14v9H1z M1 4l7 5 7-5" fill="none" stroke="#3c5a25" stroke-width="1.6"/></svg>
        <span>hwhitaker@brookridgegolfclub.com</span>
      </li>
      <li>
        <svg viewBox="0 0 16 16" aria-hidden="true"><path d="M8 1a5 5 0 0 1 5 5c0 4-5 9-5 9S3 10 3 6a5 5 0 0 1 5-5zm0 3a2 2 0 1 0 0 4 2 2 0 0 0 0-4z"/></svg>
        <span class="address">2208 Linden Hill Road<br>Carrow MD 21390</span>
      </li>
    </ul>
  </div>
</section>

<section class="card card--back" aria-label="Business card, photo side">
  <div class="frame">
    <span class="frame__corner frame__corner--tl"></span>
    <span class="frame__corner frame__corner--tr"></span>
    <span class="frame__corner frame__corner--bl"></span>
    <span class="frame__corner frame__corner--br"></span>
  </div>
  <div class="photo" role="img" aria-label="Photograph of a bride in a lace gown with a long train on the carpeted grand staircase of the historic manor"></div>
  <div class="brand brand--overlay">
    <span class="brand__name">The Manor at Brookridge Golf Club</span>
    <span class="brand__mark"></span>
  </div>
</section>

</body>
</html>
```